Business card logo/design needed

I need a new and fresh business card to get my name out there.
I have made plenty before and have a logo but I dont think it is sending the right message across.
I am a personal trainer running a small online business designed to cut the cost of training by taking it online, allowing you to purchase training over the net, through the help of Skype and video uploads.
You can personalized programs hand written for you or more general programs aimed at your goals.
Our goal is to get everyone to look like and behave like an athlete because there is no point in being in shape if you cant do anything with that body.
I also have a strong background in sports, having played low level college basketball in america and worked as a strength and conditioning coach. I dont like running or slow cardio, I am more focused on weights and functional training for aerobic fitness.
I am young for what I do, but I have lot of knowledge and I need something that says that I am not your standard drill sergeant trainer but someone who will truly help you reach your goals.
My curent logo text is "the climb to the top" but I am not set on that.

Industry/Entity Type

Personal Trainer

Contact Information for Business Card

Desmond Quilby
Summit Forge Motion
Personal trainer
Strength and conditioning coach
0481 552 709
www.summitforgemotion.example

```html
<!DOCTYPE html>
<html lang="en">
<head>
<meta charset="utf-8">
<title>Summit Forge Motion – Business Card</title>
<link rel="stylesheet" href="https://fonts.googleapis.com/css2?family=Josefin+Sans:wght@400&family=Questrial&family=Montserrat:wght@700&display=swap">
<style>
  :root {
    --paper: #ffffff;
    --frame: #1a1a1a;
    --card-edge: #555555;
    --brand-red: #ff0a0a;
    --brand-blue: #0a3cff;
    --brand-cyan: #00f0f0;
    --contact-blue: #0a40ff;
  }
  html, body {
    margin: 0;
    padding: 0;
    width: 1200px;
    height: 1000px;
    overflow: hidden;
    background: var(--paper);
  }
  .canvas {
    position: relative;
    width: 1200px;
    height: 1000px;
    box-sizing: border-box;
    border: 2px solid var(--frame);
    background: var(--paper);
  }
  .card {
    position: absolute;
    left: 216px;
    top: 279px;
    width: 770px;
    height: 444px;
    box-sizing: border-box;
    border: 1px solid var(--card-edge);
    background: var(--paper);
  }
  .card > * {
    position: absolute;
    margin: 0;
    line-height: 1;
    white-space: nowrap;
  }
  .brand-name {
    left: 66px;
    top: 62px;
    font-family: "Josefin Sans", sans-serif;
    font-weight: 400;
    font-size: 44px;
    letter-spacing: -0.01em;
    text-transform: uppercase;
    color: var(--brand-red);
  }
  .person-name {
    left: 65px;
    top: 190px;
    font-family: "Questrial", sans-serif;
    font-size: 29px;
    letter-spacing: 0.24em;
  }
  .person-name .given { color: var(--brand-blue); }
  .person-name .family { color: var(--brand-red); }
  .roles {
    left: 63px;
    top: 237px;
    font-family: "Questrial", sans-serif;
    font-size: 20px;
    line-height: 27px;
    color: var(--brand-cyan);
  }
  .contact {
    left: 64px;
    top: 345px;
    font-family: "Montserrat", sans-serif;
    font-weight: 700;
    font-size: 20px;
    line-height: 32px;
    color: var(--contact-blue);
  }
  .roles span, .contact span { display: block; }
</style>
</head>
<body>
  <main class="canvas">
    <section class="card" aria-label="Business card front">
      <h1 class="brand-name">Summit Forge Motion</h1>
      <h2 class="person-name"><span class="given">Desmond</span> <span class="family">Quilby</span></h2>
      <p class="roles">
        <span>Personal trainer</span>
        <span>Strength and conditioning coach</span>
      </p>
      <p class="contact">
        <span class="phone">0481 552 709</span>
        <span class="web">www.summitforgemotion.example</span>
      </p>
    </section>
  </main>
</body>
</html>
```